Aunt Ruwaida's Bakery

I am about to create a luxury boutique that specializes in cake baking and cupcake
and ready for parties and special events and order delivery
the logo has already made

Industry/Entity Type

Boutique

Contact Information for Business Card

Email:auntruwaidasbakery@mailvelo.com
Instagram: aunt_ruwaida_bakery
Twitter: xxxxxxx
WhatsApp: xxxxxxx

Requirements
Must have
• luxury design

```html
<!DOCTYPE html>
<html lang="en">
<head>
<meta charset="utf-8">
<title>Aunt Ruwaida's Bakery – Business Card</title>
<link rel="stylesheet" href="https://fonts.googleapis.com/css2?family=PT+Sans:wght@400;700&display=swap">
<style>
  :root {
    --backdrop: #3b3b3b;
    --rose: #d291a3;
    --paper: #f7f7f7;
    --ink-white: #ffffff;
    --ink-grey: #6f6f6f;
  }
  html, body { margin: 0; padding: 0; overflow: hidden; }
  body { width: 1200px; height: 750px; background: var(--backdrop); position: relative; font-family: "PT Sans", sans-serif; }

  .card { position: absolute; width: 352px; height: 352px; border-radius: 50%; top: 182px; }
  .card-front { left: 220px; background: var(--rose); color: var(--ink-white); }
  .card-back { left: 608px; background: var(--paper); box-shadow: inset 0 0 0 4px var(--rose); }

  .card-front .inner-ring {
    position: absolute; inset: 5px; border-radius: 50%;
    border: 2px solid var(--ink-white);
  }
  .brand-lockup {
    position: absolute; left: 0; right: 0; display: flex;
    justify-content: center; align-items: center; gap: 8px;
  }
  .brand-lockup.front { top: 58px; }
  .brand-lockup.back { top: 161px; gap: 10px; }
  .brand-seal { border-radius: 50%; flex: none; box-sizing: border-box; }
  .front .brand-seal { width: 30px; height: 30px; border: 3px solid var(--ink-white); }
  .back .brand-seal { width: 30px; height: 30px; background: var(--rose); }
  .brand-name { font-weight: 400; white-space: nowrap; }
  .front .brand-name { font-size: 15px; color: var(--ink-white); }
  .back .brand-name { font-size: 24px; color: var(--ink-grey); }

  .rule { position: absolute; height: 2px; background: var(--ink-white); }
  .rule-top { left: 52px; width: 248px; top: 104px; }
  .rule-mid { left: 52px; width: 248px; top: 166px; }
  .rule-bottom { left: 88px; width: 176px; top: 304px; }

  .person-name {
    position: absolute; left: 0; right: 0; top: 111px; text-align: center;
    font-size: 21px; font-weight: 700;
  }
  .person-role {
    position: absolute; left: 0; right: 0; top: 139px; text-align: center;
    font-size: 15px;
  }
  .contact-list {
    position: absolute; left: 0; right: 0; top: 178px; margin: 0; padding: 0;
    list-style: none; text-align: center; font-size: 14px; line-height: 23.5px;
  }
  .contact-list li { display: flex; justify-content: center; align-items: center; gap: 5px; }
  .contact-list svg { width: 13px; height: 13px; flex: none; }
  .social-dot { width: 11px; height: 11px; border-radius: 50%; border: 1.6px solid var(--ink-white); box-sizing: border-box; flex: none; }
</style>
</head>
<body>
  <section class="card card-front">
    <div class="inner-ring"></div>
    <div class="brand-lockup front">
      <span class="brand-seal"></span>
      <span class="brand-name">Aunt Ruwaida's Bakery</span>
    </div>
    <div class="rule rule-top"></div>
    <div class="person-name">Mara Lindqvist</div>
    <div class="person-role">CEO/Founder</div>
    <div class="rule rule-mid"></div>
    <ul class="contact-list">
      <li>
        <svg viewBox="0 0 24 24" aria-hidden="true"><path fill="#fff" d="M6.6 10.8a15 15 0 0 0 6.6 6.6l2.2-2.2c.3-.3.7-.4 1-.2 1.1.4 2.3.6 3.6.6.6 0 1 .4 1 1V20c0 .6-.4 1-1 1A17 17 0 0 1 3 4c0-.6.4-1 1-1h3.5c.6 0 1 .4 1 1 0 1.3.2 2.5.6 3.6.1.3 0 .7-.2 1z"/></svg>
        <span>555 218 0476</span>
      </li>
      <li>
        <svg viewBox="0 0 24 24" aria-hidden="true"><rect x="2" y="5" width="20" height="14" fill="#fff"/><path d="M2 5l10 8 10-8" fill="none" stroke="#d291a3" stroke-width="2"/></svg>
        <span>auntruwaidasbakery@mailvelo.com</span>
      </li>
      <li><span class="social-dot"></span><span>aunt_ruwaida_bakery</span></li>
      <li><span class="social-dot"></span><span>auntruwaidas_bakery</span></li>
      <li><span class="social-dot"></span><span>auntruwaidasbakery</span></li>
    </ul>
    <div class="rule rule-bottom"></div>
  </section>

  <section class="card card-back">
    <div class="brand-lockup back">
      <span class="brand-seal"></span>
      <span class="brand-name">Aunt Ruwaida's Bakery</span>
    </div>
  </section>
</body>
</html>
```